Business card design needed

Family General Practitioner/ Family Physician.
Logo is the logo of the Crestmoor Guild of Family Clinicians Australia
http://kvplm.tarevo.edu.au/PictureGallery/logos/pages/CGFC%20logo_jpg.htm

Reason: Just a bit more time to make changes and the weekend for me to look at things closely and to choose. Thanks, Lumi

Thanks for all the submissions. So many of them are really works of art. Not one of them are not good. The ones that I am eliminating are the ones that I think are not suitable for me personally only, and because if I don't, it makes it very difficult to decide as many of you are also sending me slight variations of a card. I have just decided to choose a second place card too. Can't thank you all enough. Good luck, Lumi. P.S - Working today till 10 pm as the card says :-), so probably won't be able to give a feedback till late Saturday night or Sunday morning here in Sydney, Australia. 

Reason: Just added a second place to the budget and realised that Australia is ahead of the rest of the world in the time zone (only :-) - don't want to offend anyone or start a debate!! ) , so Monday deadline will mean it will be a weekend for the rest of the world. Just wanted to give everyone more time to submit their best, especially since I will be picking a second card too. Can't thank everyone enough for the submissions. P.S - Not keen on photos on the card.

Contact Information for Business Card

Dr. Lumi Harcourt M.B.B.S., F.C.G.F.C
Family General Practitioner
Address, timings, phone and fax number on the back.

Requirements
Must have
• Timings
Mon 7 am - 7 pm
Tues 7 am - 12 pm
Wed 7 am - 10 pm
Thurs 7 am - 12 pm
Fri 7 am - 8 pm
Sat 8 am - 10 pm
Sun - Off

```html
<!DOCTYPE html>
<html lang="en">
<head>
<meta charset="utf-8">
<title>Dr. Lumi Harcourt – Business Card</title>
<link rel="stylesheet" href="https://fonts.googleapis.com/css2?family=Cinzel:wght@400&family=Cabin:wght@400;500&family=Marcellus&display=swap">
<style>
  :root {
    --page-bg: #e4e5e6;
    --card-white: #ffffff;
    --teal-deep: #0b4a52;
    --teal-mid: #136a7e;
    --teal-light: #2d7fa0;
    --mist: #c9d6de;
    --ink-brown: #4a3b35;
    --ink-soft: #5d504a;
    --blue-address: #5b8fcc;
    --blue-title: #9fc4e8;
    --band-grey: #d9d2cd;
    --crest-gold: #c9a43a;
  }
  * { box-sizing: border-box; margin: 0; padding: 0; }
  html, body { width: 1200px; height: 1000px; overflow: hidden; background: var(--page-bg); }
  .canvas { position: relative; width: 1200px; height: 1000px; }

  .card {
    position: absolute; left: 230px; width: 740px; height: 452px;
    box-shadow: 0 6px 18px rgba(0,0,0,0.18); overflow: hidden;
  }
  .card--front {
    top: 30px;
    background:
      radial-gradient(ellipse 45% 60% at 62% 20%, rgba(45,127,160,0.65), transparent 70%),
      radial-gradient(ellipse 60% 50% at 70% 95%, rgba(28,100,120,0.6), transparent 70%),
      linear-gradient(100deg, #ffffff 0%, #f2f5f7 22%, var(--mist) 33%, var(--teal-mid) 45%, var(--teal-deep) 65%, #0d5663 100%);
  }
  .card--back { top: 518px; background: var(--card-white); }

  /* Front */
  .guild-mark {
    position: absolute; left: 70px; top: 170px; width: 200px;
    display: flex; align-items: center; gap: 10px;
  }
  .guild-mark__dot { width: 22px; height: 22px; border-radius: 50%; background: var(--crest-gold); flex: none; }
  .guild-mark__name { font-family: "Cabin", sans-serif; font-weight: 500; font-size: 30px; letter-spacing: 3px; color: var(--teal-deep); }

  .identity { position: absolute; left: 295px; top: 178px; color: #fff; }
  .identity__name { font-family: "Cinzel", serif; font-size: 33px; letter-spacing: 1px; line-height: 1; }
  .identity__quals { font-family: "Marcellus", serif; font-size: 15px; margin-top: 14px; letter-spacing: 0.5px; }
  .identity__role { font-family: "Cabin", sans-serif; font-size: 20px; color: var(--blue-title); margin-top: 4px; }

  /* Back */
  .hours { position: absolute; left: 52px; top: 40px; font-family: "Cabin", sans-serif; color: var(--ink-brown); }
  .hours__title { font-size: 30px; margin-bottom: 8px; }
  .hours__row {
    display: flex; align-items: baseline; height: 31px; font-size: 22px; padding-left: 10px;
    background: linear-gradient(90deg, transparent 0%, var(--band-grey) 30%, transparent 100%) no-repeat;
    background-size: var(--band, 260px) 18px; background-position: 40px 10px;
  }
  .hours__day { width: 42px; }
  .hours__start, .hours__end { display: inline-flex; align-items: baseline; }
  .hours__leader { display: inline-block; width: var(--lead); border-bottom: 2px dotted var(--ink-brown); margin: 0 2px; transform: translateY(-4px); }
  .ampm { font-size: 12px; margin-left: 1px; }
  .hours__off { font-size: 15px; margin-top: 2px; padding-left: 10px; }

  .address {
    position: absolute; right: 46px; top: 30px; text-align: right;
    font-family: "Cabin", sans-serif; font-size: 24px; line-height: 40px; color: var(--blue-address);
  }
  .address span { display: block; }
  .contact { position: absolute; left: 62px; bottom: 34px; font-family: "Cabin", sans-serif; color: var(--ink-soft); display: flex; align-items: baseline; gap: 18px; }
  .contact__tel { font-size: 40px; letter-spacing: 1px; }
  .contact__fax { font-size: 19px; }
</style>
</head>
<body>
<div class="canvas">

  <section class="card card--front" aria-label="Business card front">
    <div class="guild-mark">
      <span class="guild-mark__dot"></span>
      <span class="guild-mark__name">CGFC</span>
    </div>
    <div class="identity">
      <h1 class="identity__name">Dr. Lumi Harcourt</h1>
      <p class="identity__quals">M.B.B.S., F.C.G.F.C</p>
      <p class="identity__role">Family General Practitioner</p>
    </div>
  </section>

  <section class="card card--back" aria-label="Business card back">
    <div class="hours">
      <h2 class="hours__title">Working hours</h2>
      <div class="hours__row" style="--band:240px"><span class="hours__day">M</span>7<span class="ampm">AM</span><span class="hours__leader" style="--lead:70px"></span>7<span class="ampm">PM</span></div>
      <div class="hours__row" style="--band:280px"><span class="hours__day">Tu</span>7<span class="ampm">AM</span><span class="hours__leader" style="--lead:30px"></span>12<span class="ampm">PM</span></div>
      <div class="hours__row" style="--band:310px"><span class="hours__day">W</span>7<span class="ampm">AM</span><span class="hours__leader" style="--lead:150px"></span>10<span class="ampm">PM</span></div>
      <div class="hours__row" style="--band:240px"><span class="hours__day">Th</span>7<span class="ampm">AM</span><span class="hours__leader" style="--lead:30px"></span>12<span class="ampm">PM</span></div>
      <div class="hours__row" style="--band:300px"><span class="hours__day">F</span>7<span class="ampm">AM</span><span class="hours__leader" style="--lead:95px"></span>8<span class="ampm">PM</span></div>
      <div class="hours__row" style="--band:320px"><span class="hours__day">Sa</span>8<span class="ampm">AM</span><span class="hours__leader" style="--lead:130px"></span>10<span class="ampm">PM</span></div>
      <p class="hours__off">Sunday Off</p>
    </div>

    <address class="address" style="font-style:normal">
      <span>Upper Level,</span>
      <span>Arcadia Court,</span>
      <span style="line-height:28px;margin-top:6px">Brindle Quay</span>
      <span style="line-height:28px;margin-bottom:6px">Shopping Centre,</span>
      <span>Marlow Heights,</span>
      <span>NSW 2169.</span>
    </address>

    <div class="contact">
      <span class="contact__tel">Tel: 02 8417 3600</span>
      <span class="contact__fax">Fax: 028417 3622</span>
    </div>
  </section>

</div>
</body>
</html>
```